The Quiet Hinge Mending Ledger

I am making a journal for tracking pain symptoms for TMJ (Jaw) pain. I have the cover designed and I just need the journal page designed that will repeat throughout the journal. The journal is the image on the left of the bundle. The page I would like to be developed is the picture that I hand sketched out. It should be a 6 x 9 page, similar to the attached example. Greyscale, no color. Thank you!

Target Market(s)

20-55 year old women

Industry/Entity Type

Healthcare

Colors

Designer to choose only greyscale colors for use in the design.

Requirements
Must have
• A neat, well-designed page with the content I have sketched out by hand.
Nice to have
• Creative display of the content I provided and development of the pain scale and pain diagram faces in a professional looking way.

```html
<!DOCTYPE html>
<html lang="en">
<head>
<meta charset="utf-8">
<title>The Quiet Hinge Mending Ledger – Daily Page</title>
<link href="https://fonts.googleapis.com/css2?family=Open+Sans:wght@400;600;700&display=swap" rel="stylesheet">
<style>
:root{
  --ink:#3a3a3a;
  --mid:#8a8a8a;
  --band:#8c8c8c;
  --cell:#dedede;
  --cell-dark:#cfcfcf;
  --line:#9a9a9a;
  --paper:#ffffff;
}
*{box-sizing:border-box;margin:0;padding:0}
html,body{width:800px;height:1200px;overflow:hidden;background:var(--paper)}
body{font-family:"Open Sans",Arial,sans-serif;color:var(--ink);position:relative}
.abs{position:absolute}

.brand{left:33px;top:28px;display:flex;align-items:center;gap:14px}
.brand-dot{width:70px;height:70px;border-radius:50%;background:var(--mid)}
.brand-name{font-size:30px;line-height:1.05;font-weight:600;color:var(--mid);width:170px}

.date-field{left:484px;top:89px;width:288px;height:22px;background:var(--cell);font-size:13px;padding:2px 8px}

.band{left:33px;width:739px;height:26px;background:var(--band);color:#fff;font-weight:700;font-size:13px;
  text-align:center;line-height:26px;border-radius:13px 13px 0 0;text-transform:uppercase;letter-spacing:.3px}

.session-table{left:33px;top:170px;width:739px;display:grid;grid-template-columns:1fr 1fr;gap:0 6px}
.session-half{display:grid;grid-template-columns:38px 1fr 1fr 1fr;gap:3px}
.session-half span{height:20px;background:var(--cell);font-size:12px;padding-left:6px;line-height:20px}
.session-half .head{background:var(--cell-dark);text-align:center;padding:0}
.session-half .num{background:transparent}

.scale-line{left:89px;top:320px;width:683px;height:2px;background:var(--line)}
.scale-num{top:311px;width:22px;text-align:center;font-size:13px;background:#fff}
.mood{top:338px;width:48px;height:48px;border-radius:50%;background:radial-gradient(circle at 40% 35%,#eee,#bdbdbd)}
.mood-label{top:392px;width:130px;text-align:center;font-size:13px;color:var(--mid)}

.zone{top:432px;width:96px;height:118px;border-radius:44px 44px 36px 36px;background:linear-gradient(#f2f2f2,#c4c4c4)}
.zone-label{top:552px;width:110px;text-align:center;font-size:11px}
.zone-scale{top:568px;width:110px}

.change-list{left:657px;top:440px;display:flex;flex-direction:column;gap:8px}
.change-list .gap{height:8px}
.opt{display:flex;align-items:center;gap:8px;font-size:12px}
.box{width:15px;height:15px;border:1.5px solid var(--mid);background:#fff;flex:none}

.grid3{left:33px;width:739px;display:grid;grid-template-columns:1fr 1fr 1fr;gap:4px 6px}
.grid3 .opt{background:var(--cell);height:22px;padding-left:10px}

.state-row{left:33px;top:758px;width:739px;display:grid;grid-template-columns:1fr 1fr 1fr;background:var(--cell);height:56px;padding:8px 16px;font-size:12px}
.state{display:flex;gap:10px;align-items:flex-start}
.state-q{width:72px;line-height:1.3}
.state-opts{display:flex;flex-direction:column;gap:6px}

.notes{left:33px;top:1034px;width:739px;display:flex;flex-direction:column;gap:5px}
.notes div{height:22px;background:var(--cell)}
</style>
</head>
<body>

<div class="abs brand"><div class="brand-dot"></div><div class="brand-name">The Quiet Hinge</div></div>
<div class="abs date-field">Date</div>

<div class="abs band" style="top:140px">Date</div>
<div class="abs session-table">
  <div class="session-half">
    <span class="num"></span><span class="head">begin</span><span class="head">end</span><span class="head">duration</span>
    <span>1</span><span></span><span></span><span></span>
    <span>2</span><span></span><span></span><span></span>
    <span>3</span><span></span><span></span><span></span>
  </div>
  <div class="session-half">
    <span class="num"></span><span class="head">begin</span><span class="head">end</span><span class="head">duration</span>
    <span>4</span><span></span><span></span><span></span>
    <span>5</span><span></span><span></span><span></span>
    <span>6</span><span></span><span></span><span></span>
  </div>
</div>

<div class="abs band" style="top:281px">Saverity of pain</div>
<div class="abs scale-line"></div>
<span class="abs scale-num" style="left:80px">1</span>
<span class="abs scale-num" style="left:155px">2</span>
<span class="abs scale-num" style="left:230px">3</span>
<span class="abs scale-num" style="left:305px">4</span>
<span class="abs scale-num" style="left:380px">5</span>
<span class="abs scale-num" style="left:455px">6</span>
<span class="abs scale-num" style="left:530px">7</span>
<span class="abs scale-num" style="left:605px">8</span>
<span class="abs scale-num" style="left:680px">9</span>
<span class="abs scale-num" style="left:750px">10</span>

<div class="abs mood" style="left:50px" role="img" aria-label="No pain face icon"></div>
<div class="abs mood" style="left:146px" role="img" aria-label="Mild pain face icon"></div>
<div class="abs mood" style="left:271px" role="img" aria-label="Moderate pain face icon"></div>
<div class="abs mood" style="left:410px" role="img" aria-label="Severe pain face icon"></div>
<div class="abs mood" style="left:552px" role="img" aria-label="Very severe pain face icon"></div>
<div class="abs mood" style="left:692px" role="img" aria-label="Worst pain possible face icon"></div>
<span class="abs mood-label" style="left:9px">no pain</span>
<span class="abs mood-label" style="left:105px">mild pain</span>
<span class="abs mood-label" style="left:230px">moderate pain</span>
<span class="abs mood-label" style="left:369px">severe pain</span>
<span class="abs mood-label" style="left:511px">very severe pain</span>
<span class="abs mood-label" style="left:660px;width:150px">worst pain possible</span>

<div class="abs zone" style="left:41px" role="img" aria-label="Head diagram marking the jaw joint"></div>
<div class="abs zone" style="left:155px" role="img" aria-label="Head diagram marking the jaw muscles"></div>
<div class="abs zone" style="left:275px" role="img" aria-label="Head diagram marking the neck"></div>
<div class="abs zone" style="left:395px" role="img" aria-label="Head diagram marking forehead tension"></div>
<div class="abs zone" style="left:515px" role="img" aria-label="Head diagram marking the teeth"></div>
<span class="abs zone-label" style="left:34px">Joint</span>
<span class="abs zone-label" style="left:148px">Muscles</span>
<span class="abs zone-label" style="left:268px">Neck</span>
<span class="abs zone-label" style="left:388px">Tension</span>
<span class="abs zone-label" style="left:508px">Teeth</span>

<svg class="abs" style="left:34px;top:568px" width="600" height="22" font-family="Open Sans, sans-serif" font-size="7" fill="#3a3a3a">
  <defs>
    <g id="mini-scale">
      <line x1="2" y1="19" x2="104" y2="19" stroke="#3a3a3a" stroke-width="1"/>
      <g stroke="#3a3a3a" stroke-width="1">
        <line x1="4" y1="12" x2="4" y2="19"/><line x1="14" y1="12" x2="14" y2="19"/><line x1="24" y1="12" x2="24" y2="19"/>
        <line x1="34" y1="12" x2="34" y2="19"/><line x1="44" y1="12" x2="44" y2="19"/><line x1="54" y1="12" x2="54" y2="19"/>
        <line x1="64" y1="12" x2="64" y2="19"/><line x1="74" y1="12" x2="74" y2="19"/><line x1="84" y1="12" x2="84" y2="19"/>
        <line x1="94" y1="12" x2="94" y2="19"/><line x1="104" y1="12" x2="104" y2="19"/>
      </g>
      <text x="1" y="8">1 2 3 4 5 6 7 8 9 10</text>
    </g>
  </defs>
  <use href="#mini-scale" x="0"/>
  <use href="#mini-scale" x="114"/>
  <use href="#mini-scale" x="234"/>
  <use href="#mini-scale" x="354"/>
  <use href="#mini-scale" x="474"/>
</svg>

<div class="abs change-list">
  <label class="opt"><span class="box"></span>increased</label>
  <label class="opt"><span class="box"></span>decreased</label>
  <label class="opt"><span class="box"></span>no change</label>
  <div class="gap"></div>
  <label class="opt"><span class="box"></span>increased</label>
  <label class="opt"><span class="box"></span>decreased</label>
  <label class="opt"><span class="box"></span>no change</label>
</div>

<div class="abs band" style="top:609px">Triggers</div>
<div class="abs grid3" style="top:639px">
  <label class="opt"><span class="box"></span>sleep</label>
  <label class="opt"><span class="box"></span>weather</label>
  <label class="opt"><span class="box"></span>PMS /menstrution</label>
  <label class="opt"><span class="box"></span>first thing AM</label>
  <label class="opt"><span class="box"></span>eating</label>
  <label class="opt"><span class="box"></span>stress at home</label>
  <label class="opt"><span class="box"></span>clenching</label>
  <label class="opt"><span class="box"></span>work</label>
  <label class="opt"><span class="box"></span>stress at work</label>
  <label class="opt"><span class="box"></span>insomnia</label>
  <label class="opt"><span class="box"></span>opening wide yawn</label>
  <label class="opt"><span class="box"></span>other</label>
</div>

<div class="abs state-row">
  <div class="state"><span class="state-q">My jaw was:</span>
    <div class="state-opts"><label class="opt"><span class="box"></span>relaxed</label><label class="opt"><span class="box"></span>clenched</label></div></div>
  <div class="state"><span class="state-q">My neck / sholders were:</span>
    <div class="state-opts"><label class="opt"><span class="box"></span>relaxed</label><label class="opt"><span class="box"></span>tense</label></div></div>
  <div class="state"><span class="state-q">My breathing was:</span>
    <div class="state-opts"><label class="opt"><span class="box"></span>shallow</label><label class="opt"><span class="box"></span>deep/relaxed</label></div></div>
</div>

<div class="abs band" style="top:845px">Relief measures</div>
<div class="abs grid3" style="top:875px">
  <label class="opt"><span class="box"></span>deep breathing</label>
  <label class="opt"><span class="box"></span>medication</label>
  <label class="opt"><span class="box"></span>mindful reset</label>
  <label class="opt"><span class="box"></span>teeth apart/relax jaw</label>
  <label class="opt"><span class="box"></span>rest</label>
  <label class="opt"><span class="box"></span>stabilization exercise</label>
  <label class="opt"><span class="box"></span>self - massage</label>
  <label class="opt"><span class="box"></span>gentle streching</label>
  <label class="opt"><span class="box"></span>other</label>
  <label class="opt"><span class="box"></span>heat / cold</label>
  <label class="opt"><span class="box"></span>positive correction</label>
  <label class="opt"><span class="box"></span></label>
</div>

<div class="abs band" style="top:1004px">Notes and plan to void triggers</div>
<div class="abs notes"><div></div><div></div><div></div><div></div><div></div></div>

</body>
</html>
```